Core Values Poster for Healthcare company

Trying to Create a core values poster for my company. Healthcare Company - We have Neurosurgery, Pain Management, Physical Therapy, Occupational Therapy, Rehab, Imaging, and psychology so far and we are growing fast.

Core Values would Include - (Execution), (Loyalty), (Innovation), (Synergy), (Growth-Oriented), (Ethics & Integrity), (Love), and (Energy)

Please incorporate the Company Logo which is on the website and I have included it in my uploads. As long as the logo stays blue it does not need a gradient effect.

I like the posters made for this contest : https://pinlarkstudio.com.au/flyer-work/briefs/build-team-ideals-flyer-580316

This picture should be memorable so people know our Core Values

Target Market(s)

Staff in the company

Colors

Designer to choose colors to be used in the design.

Requirements
Must have
• Logo
Nice to have
• Pictures for each core value

```html
<!DOCTYPE html>
<html lang="en">
<head>
<meta charset="utf-8">
<title>Core Values Poster Concepts</title>
<link rel="stylesheet" href="https://fonts.googleapis.com/css2?family=Bebas+Neue&family=Oswald:wght@400;500;600&display=swap">
<style>
  :root{
    --stage:#5b5b5b;
    --paper:#cdd6e0;
    --wheel-blue:#2677a9;
    --divider:#dbe3ec;
    --ink-white:#ffffff;
    --brand-blue:#2b79a8;
    --banner-light:#2f9bd0;
    --banner-light-dark:#1f6f9c;
    --banner-deep:#0f4d78;
    --banner-navy:#123653;
    --c-execution:#f7941d;
    --c-innovation:#f6c532;
    --c-synergy:#9dbb36;
    --c-growth:#29bfd2;
    --c-ethics:#153f63;
    --c-energy:#d9244c;
    --c-love:#e8408c;
    --c-loyalty:#8c3b8c;
    --hub-ring:#b9c6d3;
    --hub-fill:#e6ecf2;
  }
  *{margin:0;padding:0;box-sizing:border-box}
  html,body{width:1200px;height:483px;overflow:hidden;background:var(--stage)}
  .stage{position:relative;width:1200px;height:483px}
  .poster{position:absolute;top:20px;width:382px;height:442px;background:var(--paper)}
  .poster--ribbon{left:10px}
  .poster--colour{left:410px}
  .poster--arch{left:808px}
  .poster svg{display:block;width:382px;height:442px}
  .value-label{font-family:"Oswald",sans-serif;font-weight:500;font-size:13px;fill:var(--ink-white);text-anchor:middle;letter-spacing:.1px}
  .banner-title{font-family:"Bebas Neue","Oswald",sans-serif;font-size:31px;letter-spacing:5px;fill:var(--ink-white)}
  .banner-title--flat{font-size:25px;letter-spacing:5px}
  .brand-name{font-family:"Oswald",sans-serif;font-weight:400;font-size:25px;letter-spacing:1.5px;fill:var(--brand-blue)}
  .wedge-blue{fill:var(--wheel-blue)}
  .divider{fill:none;stroke:var(--divider);stroke-width:2}
  .icon-glyph{fill:none;stroke:var(--ink-white);stroke-width:1.4;stroke-linecap:round;stroke-linejoin:round}
  .icon-solid{fill:var(--ink-white)}
  .wheel{filter:drop-shadow(2px 4px 3px rgba(30,60,90,.35))}
</style>
</head>
<body>
<div class="stage">

  <svg width="0" height="0" style="position:absolute" aria-hidden="true">
    <defs>
      <path id="wedge" d="M0,0 L0,-140 L57,-139 L99,-99 Z" stroke-linejoin="round"/>
      <path id="ring-seg" d="M0,0 L0,-70 L27,-65 L49.5,-49.5 Z"/>
      <g id="dividers">
        <line x1="0" y1="0" x2="0" y2="-142"/>
      </g>
      <linearGradient id="g-execution" x1="0" y1="0" x2="1" y2="1"><stop offset="0" stop-color="#f9a531"/><stop offset="1" stop-color="#e4641a"/></linearGradient>
      <linearGradient id="g-innovation" x1="0" y1="0" x2="1" y2="1"><stop offset="0" stop-color="#fbd24a"/><stop offset="1" stop-color="#f1b51f"/></linearGradient>
      <linearGradient id="g-synergy" x1="0" y1="0" x2="1" y2="1"><stop offset="0" stop-color="#a9c63e"/><stop offset="1" stop-color="#7ea12c"/></linearGradient>
      <linearGradient id="g-growth" x1="0" y1="0" x2="1" y2="1"><stop offset="0" stop-color="#1b9fbd"/><stop offset="1" stop-color="#34d1dc"/></linearGradient>
      <linearGradient id="g-ethics" x1="0" y1="0" x2="1" y2="1"><stop offset="0" stop-color="#0f5686"/><stop offset="1" stop-color="#0e2a44"/></linearGradient>
      <linearGradient id="g-energy" x1="0" y1="0" x2="1" y2="1"><stop offset="0" stop-color="#e33050"/><stop offset="1" stop-color="#b81a3f"/></linearGradient>
      <linearGradient id="g-love" x1="0" y1="0" x2="1" y2="1"><stop offset="0" stop-color="#f04a96"/><stop offset="1" stop-color="#d8307a"/></linearGradient>
      <linearGradient id="g-loyalty" x1="0" y1="0" x2="1" y2="1"><stop offset="0" stop-color="#9a4496"/><stop offset="1" stop-color="#7a3180"/></linearGradient>
      <linearGradient id="g-banner-flat" x1="0" y1="0" x2="1" y2="0"><stop offset="0" stop-color="#0f5b8c"/><stop offset="1" stop-color="#0f2c47"/></linearGradient>
      <linearGradient id="g-banner-arch" x1="0" y1="0" x2="1" y2="0"><stop offset="0" stop-color="#1a5e8c"/><stop offset="1" stop-color="#102d48"/></linearGradient>
      <radialGradient id="g-hub" cx=".5" cy=".45" r=".6"><stop offset="0" stop-color="#eef2f6"/><stop offset="1" stop-color="#d3dce5"/></radialGradient>

      <g id="hub">
        <circle r="45" fill="var(--hub-ring)"/>
        <circle r="41" fill="url(#g-hub)" role="img" aria-label="Rocket line icon at the centre of the wheel"/>
      </g>

      <g id="ring">
        <use href="#ring-seg" fill="var(--c-execution)"/>
        <use href="#ring-seg" fill="var(--c-innovation)" transform="rotate(45)"/>
        <use href="#ring-seg" fill="var(--c-synergy)" transform="rotate(90)"/>
        <use href="#ring-seg" fill="var(--c-growth)" transform="rotate(135)"/>
        <use href="#ring-seg" fill="var(--c-ethics)" transform="rotate(180)"/>
        <use href="#ring-seg" fill="var(--c-energy)" transform="rotate(225)"/>
        <use href="#ring-seg" fill="var(--c-love)" transform="rotate(270)"/>
        <use href="#ring-seg" fill="var(--c-loyalty)" transform="rotate(315)"/>
      </g>

      <g id="divider-set" class="divider">
        <line x1="0" y1="-44" x2="0" y2="-142"/>
        <line x1="0" y1="-44" x2="0" y2="-142" transform="rotate(45)"/>
        <line x1="0" y1="-44" x2="0" y2="-142" transform="rotate(90)"/>
        <line x1="0" y1="-44" x2="0" y2="-142" transform="rotate(135)"/>
        <line x1="0" y1="-44" x2="0" y2="-142" transform="rotate(180)"/>
        <line x1="0" y1="-44" x2="0" y2="-142" transform="rotate(225)"/>
        <line x1="0" y1="-44" x2="0" y2="-142" transform="rotate(270)"/>
        <line x1="0" y1="-44" x2="0" y2="-142" transform="rotate(315)"/>
      </g>

      <g id="labels">
        <text class="value-label" x="144" y="158">LOYALTY</text>
        <text class="value-label" x="232" y="158">EXECUTION</text>
        <text class="value-label" x="287" y="213">INNOVATION</text>
        <text class="value-label" x="290" y="284">SYNERGY</text>
        <text class="value-label" x="230" y="330">GROWTH</text>
        <text class="value-label" x="230" y="346">ORIENTED</text>
        <text class="value-label" x="150" y="330">ETHICS &amp;</text>
        <text class="value-label" x="150" y="346">INTEGRITY</text>
        <text class="value-label" x="102" y="286">ENERGY</text>
        <text class="value-label" x="97" y="212">LOVE</text>
      </g>

      <g id="icon-loyalty"><circle r="10" fill="var(--c-loyalty)" stroke="#fff" stroke-width="1.5"/><circle r="5" class="icon-glyph"/></g>
      <g id="icon-execution"><circle r="10" fill="var(--c-execution)" stroke="#fff" stroke-width="1.5"/><circle r="5.5" class="icon-glyph"/><path d="M-1.5,-2.5 L2.5,0 L-1.5,2.5 Z" class="icon-solid"/></g>
      <g id="icon-innovation"><circle r="10" fill="var(--c-innovation)" stroke="#fff" stroke-width="1.5"/><circle cy="-1.5" r="3.8" class="icon-glyph"/><path d="M-1.8,3.5 H1.8 M-1.2,5.5 H1.2" class="icon-glyph"/></g>
      <g id="icon-synergy"><circle r="10" fill="var(--c-synergy)" stroke="#fff" stroke-width="1.5"/><circle cx="-2.2" r="3.8" class="icon-glyph"/><circle cx="2.2" r="3.8" class="icon-glyph"/></g>
      <g id="icon-growth"><circle r="10" fill="var(--c-growth)" stroke="#fff" stroke-width="1.5"/><path d="M-5,3 L-1.5,-0.5 L1,1.5 L5,-3" class="icon-glyph"/></g>
      <g id="icon-ethics"><circle r="10" fill="var(--c-ethics)" stroke="#fff" stroke-width="1.5"/><path d="M-4,0 L-1,3 L4.5,-3" class="icon-glyph"/></g>
      <g id="icon-energy"><circle r="10" fill="var(--c-energy)" stroke="#fff" stroke-width="1.5"/><path d="M1.5,-6 L-3.5,1 H0 L-1.5,6 L3.5,-1 H0 Z" class="icon-solid"/></g>
      <g id="icon-love"><circle r="10" fill="var(--c-love)" stroke="#fff" stroke-width="1.5"/><path d="M0,4.5 C-6,0 -5,-4.5 -2.4,-4.5 C-1,-4.5 0,-3.4 0,-2.5 C0,-3.4 1,-4.5 2.4,-4.5 C5,-4.5 6,0 0,4.5 Z" class="icon-solid"/></g>

      <g id="brand">
        <rect x="-62" y="-11" width="20" height="20" fill="var(--brand-blue)"/>
        <text class="brand-name" x="-36" y="8">VANTAGE</text>
      </g>
    </defs>
  </svg>

  <!-- Concept A: blue wheel, light ribbon banner -->
  <section class="poster poster--ribbon" aria-label="Core values poster, blue wheel with ribbon banner">
    <svg viewBox="0 0 382 442">
      <g class="banner">
        <path d="M80,84 L70,100 L98,100 L96,80 Z" fill="var(--banner-light-dark)"/>
        <path d="M304,84 L314,100 L286,100 L288,80 Z" fill="var(--banner-light-dark)"/>
        <path d="M88,60 Q192,4 296,60 L296,92 Q192,36 88,92 Z" fill="var(--banner-light)"/>
        <path id="arc-a" d="M90,84 Q192,26 294,84" fill="none"/>
        <text class="banner-title" text-anchor="middle"><textPath href="#arc-a" startOffset="50%">CORE VALUES</textPath></text>
      </g>
      <g class="wheel" transform="translate(192,242)">
        <use href="#wedge" class="wedge-blue"/>
        <use href="#wedge" class="wedge-blue" transform="rotate(45)"/>
        <use href="#wedge" class="wedge-blue" transform="rotate(90)"/>
        <use href="#wedge" class="wedge-blue" transform="rotate(135)"/>
        <use href="#wedge" class="wedge-blue" transform="rotate(180)"/>
        <use href="#wedge" class="wedge-blue" transform="rotate(225)"/>
        <use href="#wedge" class="wedge-blue" transform="rotate(270)"/>
        <use href="#wedge" class="wedge-blue" transform="rotate(315)"/>
        <use href="#ring"/>
        <use href="#divider-set"/>
        <use href="#hub"/>
      </g>
      <use href="#labels"/>
      <use href="#icon-loyalty" x="140" y="114"/>
      <use href="#icon-execution" x="246" y="114"/>
      <use href="#icon-growth" x="243" y="370"/>
      <use href="#icon-ethics" x="140" y="370"/>
      <use href="#icon-energy" x="65" y="294"/>
      <use href="#icon-love" x="65" y="188"/>
      <use href="#brand" x="192" y="417"/>
    </svg>
  </section>

  <!-- Concept B: full colour wheel, flat banner -->
  <section class="poster poster--colour" aria-label="Core values poster, colour wheel with flat banner">
    <svg viewBox="0 0 382 442">
      <g class="banner">
        <polygon points="46,24 338,24 328,40 338,56 46,56 56,40" fill="url(#g-banner-flat)"/>
        <text class="banner-title banner-title--flat" x="192" y="49" text-anchor="middle">CORE VALUES</text>
      </g>
      <g class="wheel" transform="translate(192,242)">
        <use href="#wedge" fill="url(#g-execution)"/>
        <use href="#wedge" fill="url(#g-innovation)" transform="rotate(45)"/>
        <use href="#wedge" fill="url(#g-synergy)" transform="rotate(90)"/>
        <use href="#wedge" fill="url(#g-growth)" transform="rotate(135)"/>
        <use href="#wedge" fill="url(#g-ethics)" transform="rotate(180)"/>
        <use href="#wedge" fill="url(#g-energy)" transform="rotate(225)"/>
        <use href="#wedge" fill="url(#g-love)" transform="rotate(270)"/>
        <use href="#wedge" fill="url(#g-loyalty)" transform="rotate(315)"/>
        <use href="#ring" opacity=".85"/>
        <use href="#divider-set"/>
        <use href="#hub"/>
      </g>
      <use href="#labels"/>
      <use href="#icon-innovation" x="318" y="190"/>
      <use href="#icon-synergy" x="318" y="296"/>
      <use href="#icon-growth" x="243" y="370"/>
      <use href="#icon-ethics" x="140" y="370"/>
      <use href="#icon-energy" x="65" y="294"/>
      <use href="#icon-love" x="65" y="188"/>
      <use href="#brand" x="192" y="417"/>
    </svg>
  </section>

  <!-- Concept C: blue wheel, arched navy banner -->
  <section class="poster poster--arch" aria-label="Core values poster, blue wheel with arched banner">
    <svg viewBox="0 0 382 442">
      <g class="banner">
        <path d="M96,74 L70,96 L92,100 L88,118 L112,86 Z" fill="var(--banner-deep)"/>
        <path d="M288,74 L314,96 L292,100 L296,118 L272,86 Z" fill="var(--banner-deep)"/>
        <path d="M86,66 Q192,2 298,66 L290,96 Q192,38 94,96 Z" fill="url(#g-banner-arch)"/>
        <path id="arc-c" d="M92,87 Q192,26 292,87" fill="none"/>
        <text class="banner-title" text-anchor="middle"><textPath href="#arc-c" startOffset="50%">CORE VALUES</textPath></text>
      </g>
      <g class="wheel" transform="translate(192,242)">
        <use href="#wedge" class="wedge-blue"/>
        <use href="#wedge" class="wedge-blue" transform="rotate(45)"/>
        <use href="#wedge" class="wedge-blue" transform="rotate(90)"/>
        <use href="#wedge" class="wedge-blue" transform="rotate(135)"/>
        <use href="#wedge" class="wedge-blue" transform="rotate(180)"/>
        <use href="#wedge" class="wedge-blue" transform="rotate(225)"/>
        <use href="#wedge" class="wedge-blue" transform="rotate(270)"/>
        <use href="#wedge" class="wedge-blue" transform="rotate(315)"/>
        <use href="#ring"/>
        <use href="#divider-set"/>
        <use href="#hub"/>
      </g>
      <use href="#labels"/>
      <use href="#icon-loyalty" x="140" y="114"/>
      <use href="#icon-execution" x="246" y="114"/>
      <use href="#icon-innovation" x="318" y="190"/>
      <use href="#icon-synergy" x="318" y="296"/>
      <use href="#icon-growth" x="243" y="370"/>
      <use href="#icon-ethics" x="140" y="370"/>
      <use href="#icon-energy" x="65" y="294"/>
      <use href="#icon-love" x="65" y="188"/>
      <use href="#brand" x="192" y="417"/>
    </svg>
  </section>

</div>
</body>
</html>
```